Vornel Technologies business card design

We need a business card designed with our new logo. it would be great if the card could communicate it is a technology based company.

Target Market(s)

system integrators

Industry/Entity Type

technology, IOT

Contact Information for Business Card

Name, designation, Address, telephone number, email address

Requirements
Must have
• logo and company name
Nice to have
• something to do with technology

```html
<!DOCTYPE html>
<html lang="en">
<head>
<meta charset="utf-8">
<title>Vornel Technologies – Business Card</title>
<link rel="stylesheet" href="https://fonts.googleapis.com/css2?family=Exo+2:wght@700&family=Roboto:wght@400&display=swap">
<style>
  :root {
    --backdrop: #d8d8d8;
    --card-white: #ffffff;
    --brand-orange: #f7931e;
    --ink-dark: #3a3a3a;
    --text-light: #ffffff;
  }
  * { margin: 0; padding: 0; box-sizing: border-box; }
  html, body {
    width: 1075px;
    height: 1200px;
    overflow: hidden;
    background: var(--backdrop);
  }
  .stage {
    position: relative;
    width: 1075px;
    height: 1200px;
  }
  .card {
    position: absolute;
    left: 207px;
    width: 663px;
    height: 394px;
    border-radius: 22px;
    overflow: hidden;
  }
  .card--front { top: 188px; background: var(--card-white); }
  .card--back  { top: 638px; background: var(--brand-orange); }

  /* Tech pattern areas */
  .pattern {
    position: absolute;
    inset: 0;
  }
  .card--front .pattern {
    background:
      radial-gradient(ellipse 360px 400px at 100% 75%,
        rgba(247,147,30,0.55) 0%,
        rgba(251,201,138,0.40) 40%,
        rgba(255,255,255,0) 100%);
  }
  .card--back .pattern {
    background:
      radial-gradient(ellipse 420px 420px at 0% 40%,
        rgba(255,255,255,0.28) 0%,
        rgba(255,255,255,0.12) 55%,
        rgba(255,255,255,0) 100%);
  }

  /* Brand name */
  .brand {
    position: absolute;
    left: 38px;
    top: 96px;
    display: flex;
    align-items: center;
    gap: 12px;
  }
  .brand__mark {
    width: 26px;
    height: 26px;
    background: var(--brand-orange);
  }
  .brand__name {
    font-family: "Exo 2", sans-serif;
    font-weight: 700;
    font-size: 30px;
    line-height: 1;
    letter-spacing: 0.3px;
    color: var(--ink-dark);
    text-transform: uppercase;
  }

  /* Contact side */
  .details {
    position: absolute;
    right: 38px;
    top: 0;
    text-align: right;
    color: var(--text-light);
    font-family: Roboto, sans-serif;
  }
  .person__name {
    margin-top: 103px;
    font-family: "Exo 2", sans-serif;
    font-weight: 700;
    font-size: 26px;
    line-height: 28px;
    letter-spacing: 0.3px;
    text-transform: uppercase;
  }
  .person__role {
    font-size: 18px;
    line-height: 22px;
  }
  .contacts {
    list-style: none;
    margin-top: 60px;
    font-size: 17.5px;
    line-height: 23.5px;
  }
  .contacts li {
    display: flex;
    justify-content: flex-end;
    align-items: center;
    gap: 6px;
  }
  .contacts svg { width: 16px; height: 16px; flex: none; }
  .address {
    margin-top: 31px;
    font-size: 17.5px;
    line-height: 23.5px;
    font-style: normal;
  }
</style>
</head>
<body>
<main class="stage">

  <section class="card card--front">
    <div class="pattern" role="img" aria-label="Decorative pattern of overlapping orange outlined squares"></div>
    <div class="brand">
      <span class="brand__mark"></span>
      <span class="brand__name">Vornel Technologies</span>
    </div>
  </section>

  <section class="card card--back">
    <div class="pattern" role="img" aria-label="Decorative pattern of overlapping pale outlined squares"></div>
    <div class="details">
      <h1 class="person__name">Darren Holloway</h1>
      <p class="person__role">Managing Director</p>
      <ul class="contacts">
        <li>044-987 654 321
          <svg viewBox="0 0 16 16" aria-hidden="true"><path d="M4 1.5 6.2 4 5 5.6c.8 1.9 2.4 3.5 4.3 4.3L10.9 8.7 13.5 11l-1.3 2.4C7 13.2 2.8 9 2.6 3.8Z" fill="none" stroke="#fff" stroke-width="1.5" stroke-linejoin="round"/></svg>
        </li>
        <li>hello@vorneltech.com
          <svg viewBox="0 0 16 16" aria-hidden="true"><rect x="1" y="3" width="14" height="10" fill="#fff"/><path d="M1 3l7 6 7-6" fill="none" stroke="#f7931e" stroke-width="1.3"/></svg>
        </li>
        <li>www.vorneltech.com
          <svg viewBox="0 0 16 16" aria-hidden="true"><g fill="none" stroke="#fff" stroke-width="1.3"><circle cx="8" cy="8" r="6.5"/><ellipse cx="8" cy="8" rx="3" ry="6.5"/><path d="M1.5 8h13M2.6 4.8h10.8M2.6 11.2h10.8"/></g></svg>
        </li>
      </ul>
      <address class="address">
        58, Corvane Street, Suite 4<br>
        60318, Eastmere
      </address>
    </div>
  </section>

</main>
</body>
</html>
```